The Quiet Ledger Method - Seven Weekend Fixes

Nonfiction book about how to save on insurance. Almost one hundred measures and examples to reduce ones insurance costs.

Target Market(s)

Men/Women between 18 and 50

Industry/Entity Type

Insurance

```html
<!DOCTYPE html>
<html lang="en">
<head>
<meta charset="utf-8">
<title>The Quiet Ledger Method - Seven Weekend Fixes</title>
<link rel="stylesheet" href="https://fonts.googleapis.com/css2?family=Abel&family=Gudea:wght@400;700&family=Josefin+Sans:wght@400&display=swap">
<style>
  :root {
    --stage: #3a2823;
    --teal: #5cc6d1;
    --teal-deep: #46b7c4;
    --teal-soft: #74d0da;
    --spine-light: #9fe6ef;
    --mint: #d8efdf;
    --navy: #27297e;
    --royal: #2e4ab0;
    --royal-dark: #1f2f86;
    --royal-light: #4a66c8;
    --ice: #eaf9fa;
    --ice-shade: #bfe6ea;
    --paper: #ffffff;
    --ink: #1c2b2e;
    --placeholder: #e6e6e6;
    --placeholder-text: #b5b5b5;
  }
  * { box-sizing: border-box; margin: 0; padding: 0; }
  html, body { width: 1200px; height: 1196px; overflow: hidden; }
  body { background: var(--stage); position: relative; }

  .book-wrap {
    position: absolute; left: 65px; top: 218px;
    width: 1070px; height: 760px; display: flex;
  }

  /* Back cover */
  .back-cover {
    position: relative; width: 500px; height: 760px;
    background: linear-gradient(90deg, var(--teal-deep), var(--teal));
  }
  .back-accent {
    position: absolute; left: 40px; top: 165px; width: 115px; height: 128px;
    background: var(--mint);
  }
  .back-photo {
    position: absolute; left: 185px; top: 152px; width: 250px; height: 160px;
    background: linear-gradient(135deg, #f4f4f4, var(--placeholder));
    display: flex; align-items: center; justify-content: center; text-align: center;
    font-family: "Abel", sans-serif; font-size: 27px; line-height: 1.2;
    color: var(--placeholder-text);
  }
  .back-blurb {
    position: absolute; left: 75px; top: 345px; width: 360px;
    font-family: "Josefin Sans", sans-serif; font-size: 13.5px; line-height: 1.45;
    color: var(--ink); text-align: justify;
  }
  .back-blurb p { text-indent: 50px; margin-bottom: 22px; }

  /* Spine */
  .spine {
    width: 70px; height: 760px;
    background: linear-gradient(180deg, var(--teal) 0%, var(--teal) 55%, var(--spine-light) 100%);
    display: flex; flex-direction: column; align-items: center;
    padding: 22px 0;
    font-family: "Abel", sans-serif; color: var(--paper);
  }
  .spine-author, .spine-title { writing-mode: vertical-rl; white-space: nowrap; }
  .spine-author { font-size: 22px; }
  .spine-title { font-size: 22px; margin-top: auto; margin-bottom: 10px; }

  /* Front cover */
  .front-cover {
    position: relative; width: 500px; height: 760px;
    background: var(--paper); padding: 10px;
  }
  .front-field { position: relative; width: 100%; height: 100%; overflow: hidden; }
  .front-backdrop {
    position: absolute; inset: 0;
    background: linear-gradient(160deg, var(--teal-soft), var(--teal) 55%, var(--teal-deep));
  }
  .title-band {
    position: absolute; left: 0; right: 0; top: 110px; height: 132px;
    background: var(--mint);
  }
  .title-band svg { position: absolute; top: 16px; }
  .band-lines-left { left: 14px; }
  .band-lines-right { right: 14px; }
  .title {
    position: absolute; inset: 0;
    display: flex; flex-direction: column; align-items: center; justify-content: center;
    font-family: "Gudea", sans-serif; color: var(--navy); line-height: 1.05;
  }
  .title-top { font-size: 42px; }
  .title-main { font-size: 58px; font-weight: 700; }

  .subtitle {
    position: absolute; font-family: "Gudea", sans-serif; font-weight: 700;
    -webkit-background-clip: text; background-clip: text;
    -webkit-text-fill-color: transparent; color: transparent;
  }
  .sub-first {
    top: 268px; left: 70px; font-size: 120px; line-height: 1;
    background-image: linear-gradient(100deg,
      var(--paper) 0 24%, var(--ice-shade) 24% 46%,
      var(--ice) 46% 70%, var(--ice-shade) 70% 100%);
  }
  .sub-middle {
    top: 408px; left: 145px; font-size: 40px; line-height: 1.2;
    -webkit-text-fill-color: var(--royal); color: var(--royal);
  }
  .sub-last {
    top: 452px; left: 120px; font-size: 120px; line-height: 1;
    background-image: linear-gradient(100deg,
      var(--royal-light) 0 22%, var(--royal-dark) 22% 45%,
      var(--royal) 45% 70%, var(--royal-dark) 70% 100%);
  }

  .front-rule {
    position: absolute; left: 40px; right: 40px; top: 648px; height: 2px;
    background: linear-gradient(90deg, transparent, var(--ice), transparent);
  }
  .front-author {
    position: absolute; left: 0; right: 0; top: 668px; text-align: center;
    font-family: "Abel", sans-serif; font-size: 28px; color: var(--ice);
  }
</style>
</head>
<body>
  <main class="book-wrap">
    <section class="back-cover">
      <div class="back-accent"></div>
      <div class="back-photo">Your<br>Picture<br>Goes Here</div>
      <div class="back-blurb">
        <p>Every policy hides a quiet cost. This book walks through the bills you already pay and shows where the money slips away, one page at a time, without jargon or pressure.</p>
        <p>Nearly one hundred measures and worked examples help you compare cover, drop what you do not need and ask better questions before you renew. Each fix fits into a single weekend.</p>
        <p>Read it once, keep the checklists and let the savings add up year after year.</p>
      </div>
    </section>

    <section class="spine">
      <span class="spine-author">Martin Ehrlich</span>
      <span class="spine-title">The Quiet Ledger Method - Seven Weekend Fixes</span>
    </section>

    <section class="front-cover">
      <div class="front-field">
        <div class="front-backdrop" role="img" aria-label="Decorative light diagonal stripe pattern on teal"></div>
        <div class="title-band">
          <svg class="band-lines-left" width="30" height="100" viewBox="0 0 30 100">
            <line x1="20" y1="0" x2="2" y2="100" stroke="#27297e" stroke-width="2"/>
            <line x1="30" y1="0" x2="12" y2="100" stroke="#27297e" stroke-width="2"/>
          </svg>
          <svg class="band-lines-right" width="30" height="100" viewBox="0 0 30 100">
            <line x1="0" y1="100" x2="18" y2="0" stroke="#27297e" stroke-width="2"/>
            <line x1="10" y1="100" x2="28" y2="0" stroke="#27297e" stroke-width="2"/>
          </svg>
          <h1 class="title">
            <span class="title-top">The Quiet Ledger</span>
            <span class="title-main">Method</span>
          </h1>
        </div>
        <div class="subtitle sub-first">Seven</div>
        <div class="subtitle sub-middle">Weekend</div>
        <div class="subtitle sub-last">Fixes</div>
        <div class="front-rule"></div>
        <div class="front-author">Martin Ehrlich</div>
      </div>
    </section>
  </main>
</body>
</html>
```